Business Card Design

Lawyer
Business name "HarlowLaw"
Areas of expertise:
property
commercial
trusts
immigration
franchising
I want the following quote on the back of the card somewhere.
"Education is when you read the fine print,
experience is what you get if you don't." Miles Corbell
Probably the "areas of expertise" should be on the back also to avoid cluttering the front.
As for colours, I like the shades of blue used on qerivo.com.
The basic part of the card with the contact info needs to be white and uncluttered.
Target Market(s)
small to medium sized self employed business people
Industry/Entity Type
Business
Contact Information for Business Card
Dennis Harlow
Phone + 64 9 517 4460
Fax: + 64 9 517 4461
PO Box 742
Clevedon
Auckland 2248
NZ
email: dennis@pinecrestlegal.co.nz

```html
<!DOCTYPE html>
<html lang="en">
<head>
<meta charset="utf-8">
<title>HarlowLaw Business Card</title>
<link href="https://fonts.googleapis.com/css2?family=Open+Sans:ital,wght@0,400;0,600;0,700;1,400;1,600&display=swap" rel="stylesheet">
<style>
  :root {
    --bg: #d9dadc;
    --blue-deep: #143f96;
    --blue-mid: #0f62b8;
    --blue-bright: #0a95d8;
    --brand-blue: #0b4ea2;
    --white: #ffffff;
    --card-shadow: rgba(0, 0, 0, 0.25);
  }
  * { margin: 0; padding: 0; box-sizing: border-box; }
  html, body {
    width: 1200px; height: 900px; overflow: hidden;
    background: var(--bg);
    font-family: "Open Sans", Arial, sans-serif;
  }
  .canvas { position: relative; width: 1200px; height: 900px; }
  .card {
    position: absolute; left: 255px;
    width: 690px; height: 400px;
    overflow: hidden;
    box-shadow: 0 6px 18px var(--card-shadow);
  }
  /* Front */
  .card--front {
    top: 35px;
    background: linear-gradient(110deg, var(--blue-deep) 0%, var(--blue-mid) 55%, var(--blue-bright) 100%);
    color: var(--white);
  }
  .rail { position: absolute; left: 68px; width: 44px; background: var(--white); }
  .rail--top { top: -30px; height: 135px; border-radius: 0 0 22px 22px; }
  .rail--bottom { bottom: -30px; height: 115px; border-radius: 22px 22px 0 0; }
  .identity { position: absolute; right: 58px; top: 38px; text-align: center; }
  .identity__name { font-size: 36px; font-weight: 400; line-height: 1.1; }
  .identity__name strong { font-weight: 700; }
  .identity__role { font-size: 20px; font-weight: 600; }
  .contacts { position: absolute; left: 74px; top: 142px; list-style: none; }
  .contacts li {
    display: flex; align-items: center; height: 40px;
    font-size: 18px; font-weight: 600; letter-spacing: 0.3px;
    white-space: nowrap;
  }
  .contacts .icon {
    width: 32px; height: 32px; border-radius: 50%;
    background: var(--white); display: flex; align-items: center; justify-content: center;
    margin-right: 30px; flex: none;
  }
  .contacts svg { width: 18px; height: 18px; fill: var(--blue-deep); }
  /* Back */
  .card--back {
    top: 470px;
    background: linear-gradient(100deg, var(--blue-deep) 0%, var(--blue-mid) 55%, var(--blue-bright) 100%);
    color: var(--white);
  }
  .quote {
    position: absolute; right: 60px; top: 14px; width: 520px;
    font-size: 17px; line-height: 1.2; text-align: center;
  }
  .quote__author { display: block; text-align: right; padding-right: 40px; }
  .brand-band {
    position: absolute; left: 0; right: 0; top: 100px; height: 135px;
    background: var(--white); color: var(--brand-blue);
    display: flex; flex-direction: column; align-items: center; justify-content: center;
  }
  .brand-band__name { font-size: 40px; font-weight: 700; line-height: 1.05; letter-spacing: 0.5px; }
  .brand-band__tag { font-size: 24px; font-weight: 600; font-style: italic; }
  .expertise {
    position: absolute; left: 0; right: 0; top: 298px;
    text-align: center; font-size: 21px; font-weight: 600; letter-spacing: 0.4px;
    white-space: nowrap;
  }
</style>
</head>
<body>
<main class="canvas">
  <section class="card card--front" aria-label="Card front">
    <div class="rail rail--top"></div>
    <div class="rail rail--bottom"></div>
    <div class="identity">
      <h1 class="identity__name">Dennis <strong>Harlow</strong></h1>
      <p class="identity__role">Lawyer</p>
    </div>
    <ul class="contacts">
      <li><span class="icon"><svg viewBox="0 0 24 24"><path d="M6.6 10.8a15 15 0 0 0 6.6 6.6l2.2-2.2c.3-.3.7-.4 1-.2 1.1.4 2.3.6 3.6.6.6 0 1 .4 1 1V20c0 .6-.4 1-1 1A17 17 0 0 1 3 4c0-.6.4-1 1-1h3.5c.6 0 1 .4 1 1 0 1.3.2 2.5.6 3.6.1.3 0 .7-.2 1z"/></svg></span>+ 64 9 517 4460</li>
      <li><span class="icon"><svg viewBox="0 0 24 24"><path d="M7 3h10v4H7zM4 8h16a2 2 0 0 1 2 2v6h-4v5H6v-5H2v-6a2 2 0 0 1 2-2zm4 8v3h8v-3z"/></svg></span>+ 64 9 517 4461</li>
      <li><span class="icon"><svg viewBox="0 0 24 24"><path d="M3 5h18v14H3zm2 2v.5l7 5 7-5V7zm0 3v7h14v-7l-7 5z"/></svg></span>dennis@pinecrestlegal.co.nz</li>
      <li><span class="icon"><svg viewBox="0 0 24 24"><path d="M12 3l10 9h-3v8h-5v-6h-4v6H5v-8H2z"/></svg></span>PO Box 742 Kelvale Tarrowby 3516 NZ</li>
    </ul>
  </section>

  <section class="card card--back" aria-label="Card back">
    <p class="quote">"Education is when you read the fine print,<br>experience is what you get if you don't."<span class="quote__author">Miles Corbell</span></p>
    <div class="brand-band">
      <h2 class="brand-band__name">HarlowLaw</h2>
      <p class="brand-band__tag">"areas of expertise"</p>
    </div>
    <p class="expertise">Trusts - Property - Franchising - Commercial - Immigration</p>
  </section>
</main>
</body>
</html>
```